HOPE TABERNACLE- Premier Church Service.

Date: Sunday April 28th 2019.
Time: 10:30am-12:30pm
Venue: Blue Heron Hotel & conference Centre
4 N. Pellman Road Renton Wa 98064 USA.
Special treat at no extra cost!!!!
-Breakfast available 9am-10:15am.

-3 course Lunch available after Church.

NB: AMAZING ARRANGEMENTS FOR CHILDREN.
...........................................................................................................

EVENING JUBILEE, Wa 2019..........6:30pm-8:30pm.
" A time of high praise, deep Worship, the prophetic, Salvation, healing, miracles and more! "

...........................................................................................................................

Resident Pastors: Pastors Lou & Mary Kamau.

Guest ministers:

Apostle Daniel Otieno
Well of Mercy Sacramento, California.

THE LADY IN PINK IS THE WIFE TO THE MAN WITH THE ORANGE CLOTH IN HIS JACKET POSCKET. TRY MAKE IT COME OUT AS IF THESE TWO WERE TAKEN TOGETHER.

16-60

Designer to choose colors to be used in the design.

• -Very catchy and creative design.

```html
<!DOCTYPE html>
<html lang="en">
<head>
<meta charset="utf-8">
<title>Hope Tabernacle – Premier Church Service</title>
<link rel="stylesheet" href="https://fonts.googleapis.com/css2?family=Cinzel:wght@700&family=Great+Vibes&family=Oswald:wght@500&family=Raleway:wght@500;600&family=Roboto:wght@400;500&display=swap">
<style>
  :root {
    --page-bg: #0b0b0b;
    --ink-black: #050505;
    --panel-black: #0d0d0d;
    --band-grey: #1c1c1d;
    --gold: #e7c462;
    --gold-light: #f6df8c;
    --gold-deep: #b48a2c;
    --white: #ffffff;
    --ink-dark: #1a1408;
  }
  * { margin: 0; padding: 0; box-sizing: border-box; }
  html, body {
    width: 1200px; height: 883px; overflow: hidden;
    background: var(--page-bg);
  }
  .flyer {
    position: absolute; left: 307px; top: 27px;
    width: 585px; height: 828px;
    background: var(--ink-black);
    overflow: hidden;
    font-family: "Roboto", Arial, sans-serif;
    color: var(--white);
    text-align: center;
  }
  .abs { position: absolute; }

  /* Header */
  .header { left: 0; top: 0; width: 585px; height: 268px;
    background: radial-gradient(ellipse at 50% 55%, #1e1a10 0%, #050505 70%); }
  .photo-guest { left: 0; top: 0; width: 222px; height: 268px;
    background: linear-gradient(160deg, #2a2320 0%, #6b6f80 55%, #b7c1d6 100%); }
  .photo-resident { left: 362px; top: 0; width: 223px; height: 268px;
    background: linear-gradient(200deg, #d4a53a 0%, #b5579f 35%, #6e5a6a 70%, #2a2228 100%); }
  .title { left: 157px; top: 26px; width: 270px; z-index: 2;
    font-family: "Cinzel", "Times New Roman", serif; font-weight: 700;
    font-size: 27px; line-height: 40px; letter-spacing: 1px; white-space: nowrap;
    color: var(--gold); text-shadow: 0 1px 3px rgba(0,0,0,.8); }
  .title-rule { left: 220px; top: 116px; width: 145px; height: 12px; z-index: 2; }
  .tagline { left: 190px; top: 133px; width: 205px; font-size: 11.5px; font-weight: 500; z-index: 2; }

  /* Ministers band */
  .ministers { left: 0; top: 268px; width: 585px; height: 97px;
    background: linear-gradient(90deg, #b38b2e 0%, #f3d77f 30%, #e8c35d 60%, #f6e29a 80%, #b58c2f 100%);
    color: var(--ink-dark); font-family: "Raleway", Arial, sans-serif;
    border-top: 3px solid #fff1b8; border-bottom: 3px solid var(--gold-deep); }
  .guest { left: 14px; top: 14px; width: 252px; }
  .minister-name { font-size: 17px; font-weight: 600; }
  .minister-role { font-family: "Cinzel", serif; font-size: 10px; font-weight: 700; margin-top: 2px; }
  .minister-church { font-size: 11.5px; font-weight: 500; margin-top: 4px; }
  .resident { left: 340px; top: 14px; width: 240px; }

  /* Service section */
  .service { left: 0; top: 368px; width: 585px; height: 220px;
    background: var(--panel-black); }
  .candles-left { left: 12px; top: 418px; width: 90px; height: 182px;
    background: linear-gradient(180deg, #f2d27a 0%, #7a5c1f 60%, rgba(13,13,13,0) 100%); opacity: .55; }
  .candles-right { left: 480px; top: 418px; width: 90px; height: 182px;
    background: linear-gradient(180deg, #f2d27a 0%, #7a5c1f 60%, rgba(13,13,13,0) 100%); opacity: .55; }
  .service-date { left: 110px; top: 380px; width: 365px;
    font-family: "Oswald", "Arial Narrow", sans-serif; font-weight: 500;
    font-size: 32px; line-height: 44px; color: var(--gold); }
  .date-rule { left: 155px; height: 1px; width: 275px; background: var(--gold-deep); }
  .service-time { left: 110px; top: 434px; width: 365px; font-size: 14px; font-weight: 500; }
  .treat { left: 110px; top: 467px; width: 365px; font-family: "Raleway", sans-serif;
    font-size: 17px; font-weight: 600; color: var(--gold); }
  .meal { left: 110px; width: 365px; font-size: 13.5px; font-weight: 500; }
  .children { left: 60px; top: 557px; width: 465px; font-family: "Raleway", sans-serif;
    font-size: 15px; font-weight: 600; color: var(--gold); }

  /* Evening band */
  .evening { left: 0; top: 590px; width: 585px; height: 94px;
    background: var(--band-grey);
    border-top: 2px solid var(--gold); border-bottom: 2px solid var(--gold); }
  .evening-title { left: 0; top: 14px; width: 585px; font-family: "Raleway", sans-serif;
    font-size: 17.5px; font-weight: 600; color: var(--gold); }
  .evening-quote { left: 60px; top: 46px; width: 465px; font-family: "Raleway", sans-serif;
    font-size: 13px; line-height: 17px; font-weight: 500; }

  /* Venue */
  .venue { left: 0; top: 686px; width: 585px; height: 142px; background: var(--ink-black); }
  .venue-heading { left: 0; top: 8px; width: 585px;
    font-family: "Great Vibes", cursive; font-size: 34px; color: var(--gold); }
  .venue-rule { top: 33px; width: 80px; height: 1px; background: var(--gold-deep); }
  .venue-address { left: 0; top: 52px; width: 585px; font-size: 15px; line-height: 19px; }
  .sparkle { left: 0; top: 92px; width: 585px; height: 50px;
    background: linear-gradient(180deg, rgba(5,5,5,0) 0%, #6b4f14 45%, #d9b04b 80%, #f3d77b 100%); }
</style>
</head>
<body>
<main class="flyer">
  <section class="abs header">
    <div class="abs photo-guest" role="img" aria-label="Photo of guest minister Apostle Daniel Otieno in a light blue suit with his wife"></div>
    <div class="abs photo-resident" role="img" aria-label="Photo of Pastors Lou and Mary Kamau posed together, she in pink, he with an orange pocket square"></div>
    <h1 class="abs title">HOPE<br>TABERNACLE</h1>
    <svg class="abs title-rule" viewBox="0 0 145 12" aria-hidden="true">
      <line x1="0" y1="6" x2="145" y2="6" stroke="#c9a24a" stroke-width="1"/>
      <circle cx="72.5" cy="6" r="3" fill="#e7c462"/>
    </svg>
    <p class="abs tagline">- Premier Church Service -</p>
  </section>

  <section class="abs ministers">
    <div class="abs guest">
      <p class="minister-name">Apostle Daniel Otieno</p>
      <p class="minister-role">(Guest ministers)</p>
      <p class="minister-church">Well of Mercy Sacramento, California.</p>
    </div>
    <div class="abs resident">
      <p class="minister-name">Pastors Lou &amp; Mary Kamau</p>
    </div>
  </section>

  <section class="abs service"></section>
  <div class="abs candles-left" role="img" aria-label="Gold candelabra with three lit candles"></div>
  <div class="abs candles-right" role="img" aria-label="Gold candelabra with three lit candles"></div>
  <h2 class="abs service-date">April 28th 2019, Sunday</h2>
  <div class="abs date-rule" style="top:427px"></div>
  <p class="abs service-time">10:30am-12:30pm</p>
  <div class="abs date-rule" style="top:458px"></div>
  <p class="abs treat">Special treat at no extra cost!!!!</p>
  <p class="abs meal" style="top:501px">-Breakfast available 9am-10:15am.</p>
  <p class="abs meal" style="top:525px">-3 course Lunch available after Church.</p>
  <p class="abs children">NB: AMAZING ARRANGEMENTS FOR CHILDREN.</p>

  <section class="abs evening">
    <p class="abs evening-title">EVENING JUBILEE, Wa 2019..........6:30pm-8:30pm.</p>
    <p class="abs evening-quote">" A time of high praise, deep Worship, the prophetic,<br>Salvation, healing, miracles and more! "</p>
  </section>

  <section class="abs venue">
    <div class="abs venue-rule" style="left:180px"></div>
    <h3 class="abs venue-heading">Venue</h3>
    <div class="abs venue-rule" style="left:325px"></div>
    <p class="abs venue-address">Blue Heron Hotel &amp; conference Centre<br>4 N. Pellman Road Renton Wa 98064 USA.</p>
    <div class="abs sparkle" role="img" aria-label="Gold glitter sparkle border"></div>
  </section>
</main>
</body>
</html>
```